KRWM new business card design

We need a business card design for our established business which is Australia wide however based in Melbourne. We are a young team of Financial Planners who specialize in Insurance and Basic super advice for people like us.

We are people who help our clients get things done in a timely and cost effective manner whilst having a good time and a laugh along the way.

We would like this to have a consistent feel with our new e-brochure which i have attached from a color and font perspective.

Industry/Entity Type

Business

Requirements
Must have
• We do not need specific address details rather just the states we are in:

VIC/NSW/QLD/TAS
Nice to have
• Curved edge to mate the brochure

```html
<!DOCTYPE html>
<html lang="en">
<head>
<meta charset="utf-8">
<title>KRWM Business Card</title>
<link href="https://fonts.googleapis.com/css2?family=Arimo:wght@700&display=swap" rel="stylesheet">
<style>
  :root {
    --backdrop: #7a7a7a;
    --card-black: #050505;
    --card-white: #ffffff;
    --card-grey: #ececec;
    --brand-green: #5cc43a;
    --brand-green-dark: #2f9a2a;
    --ink: #111111;
    --paper-text: #ffffff;
  }
  html, body {
    margin: 0;
    padding: 0;
    width: 1200px;
    height: 726px;
    overflow: hidden;
    background: var(--backdrop);
    font-family: "Arimo", Arial, sans-serif;
  }
  .canvas {
    position: relative;
    width: 1200px;
    height: 726px;
    display: flex;
    align-items: center;
    justify-content: center;
    gap: 60px;
  }
  .card {
    width: 520px;
    height: 300px;
    border-radius: 26px;
    overflow: hidden;
    position: relative;
    box-sizing: border-box;
  }
  .card--front {
    background: radial-gradient(circle at 50% 40%, #1c1c1c 0%, var(--card-black) 55%);
    display: flex;
    align-items: center;
    justify-content: center;
  }
  .card--back {
    display: flex;
    background: var(--card-white);
  }
  .back-brand {
    width: 38%;
    background: var(--card-black);
    display: flex;
    align-items: center;
    justify-content: center;
  }
  .back-states {
    flex: 1;
    background: linear-gradient(180deg, var(--card-white) 0%, var(--card-grey) 100%);
    display: flex;
    align-items: center;
    padding-left: 58px;
  }
  .brand {
    display: flex;
    align-items: center;
    gap: 14px;
    color: var(--paper-text);
    font-weight: 700;
    letter-spacing: 1px;
  }
  .brand-square {
    background: var(--brand-green);
    display: block;
  }
  .brand--large { font-size: 56px; }
  .brand--large .brand-square { width: 40px; height: 40px; }
  .brand--small { font-size: 34px; gap: 10px; }
  .brand--small .brand-square { width: 24px; height: 24px; }
  .state-list {
    list-style: none;
    margin: 0;
    padding: 0;
  }
  .state {
    display: flex;
    align-items: center;
    gap: 14px;
    font-size: 20px;
    font-weight: 700;
    color: var(--ink);
    margin: 14px 0;
  }
  .state-marker {
    width: 12px;
    height: 12px;
    background: var(--brand-green);
    border: 2px solid var(--brand-green-dark);
    box-sizing: border-box;
  }
</style>
</head>
<body>
  <main class="canvas">
    <section class="card card--front" aria-label="Card front">
      <div class="brand brand--large">
        <span class="brand-square"></span>
        <span class="brand-name">KRWM</span>
      </div>
    </section>

    <section class="card card--back" aria-label="Card back">
      <div class="back-brand">
        <div class="brand brand--small">
          <span class="brand-square"></span>
          <span class="brand-name">KRWM</span>
        </div>
      </div>
      <div class="back-states">
        <ul class="state-list">
          <li class="state"><span class="state-marker"></span>Victoria</li>
          <li class="state"><span class="state-marker"></span>New South Wales</li>
          <li class="state"><span class="state-marker"></span>Queensland</li>
          <li class="state"><span class="state-marker"></span>Tasmania</li>
        </ul>
      </div>
    </section>
  </main>
</body>
</html>
```